Creative & Professional Business Card for hair salon

We are looking to update our business cards. Our salon is creative, modern, progressive and professional and looking for a design that will reflect this.

```html
<!DOCTYPE html>
<html lang="en">
<head>
<meta charset="utf-8">
<title>Silver Mist Studio – Business Card</title>
<link rel="stylesheet" href="https://fonts.googleapis.com/css2?family=Open+Sans:wght@300;400;600&display=swap">
<style>
  :root {
    --backdrop: #e9e6e2;
    --card-dark: #0b0b0c;
    --card-light: #ffffff;
    --brand-blue: #6aa3bd;
    --brand-blue-deep: #4a8fb5;
    --text-grey: #6a6a6a;
    --rule-grey: #8a8a8a;
  }
  * { margin: 0; padding: 0; box-sizing: border-box; }
  html, body { width: 1200px; height: 1000px; overflow: hidden; }
  body {
    background: var(--backdrop);
    font-family: "Open Sans", Arial, sans-serif;
    position: relative;
  }
  .card {
    position: absolute;
    left: 267px;
    width: 665px;
    height: 397px;
    border-radius: 24px;
    box-shadow: 0 6px 16px rgba(0,0,0,0.25);
  }
  .card--front { top: 74px; background: var(--card-dark); }
  .card--back  { top: 532px; background: var(--card-light); }

  .brand {
    position: absolute;
    color: var(--brand-blue);
    font-weight: 300;
    display: flex;
    align-items: center;
    gap: 14px;
  }
  .brand__dot {
    border-radius: 50%;
    background: var(--brand-blue);
    flex: none;
  }
  .brand__text { line-height: 1.1; }
  .brand__byline { display: block; text-align: right; }

  .card--front .brand { left: 120px; top: 190px; font-size: 40px; }
  .card--front .brand__dot { width: 34px; height: 34px; }
  .card--front .brand__byline { font-size: 20px; margin-top: 6px; }

  .card--back .brand { left: 38px; top: 112px; font-size: 28px; }
  .card--back .brand__dot { width: 24px; height: 24px; }
  .card--back .brand__byline { font-size: 15px; margin-top: 4px; }

  .contact { position: absolute; left: 38px; top: 214px; color: var(--text-grey); }
  .contact__name {
    color: var(--brand-blue-deep);
    font-weight: 600;
    font-size: 19px;
    letter-spacing: 0.3px;
    margin-bottom: 10px;
  }
  .contact__address { font-size: 15px; line-height: 21px; margin-left: 4px; margin-bottom: 6px; }
  .contact__line {
    display: flex; align-items: center; gap: 6px;
    font-size: 16px; line-height: 22px; margin-left: 4px;
  }
  .contact__icon { width: 14px; height: 14px; fill: var(--text-grey); flex: none; }

  .appointment {
    position: absolute; left: 343px; top: 340px;
    display: flex; gap: 10px;
    font-size: 16px; color: var(--text-grey);
  }
  .appointment__field { display: flex; align-items: flex-end; }
  .appointment__rule { display: inline-block; border-bottom: 1px solid var(--rule-grey); margin-bottom: 3px; }
  .appointment__rule--date { width: 108px; }
  .appointment__rule--time { width: 78px; }
</style>
</head>
<body>
  <section class="card card--front" aria-label="Card front">
    <div class="brand">
      <span class="brand__dot"></span>
      <span class="brand__text">Silver Mist Studio<span class="brand__byline">by Lena Marlow</span></span>
    </div>
  </section>

  <section class="card card--back" aria-label="Card back">
    <div class="brand">
      <span class="brand__dot"></span>
      <span class="brand__text">Silver Mist Studio<span class="brand__byline">by Lena Marlow</span></span>
    </div>

    <div class="contact">
      <p class="contact__name">DANIEL FERRICK</p>
      <p class="contact__address">214 Harbor Lane<br>Fairview, Ohio 44102</p>
      <p class="contact__line">
        <svg class="contact__icon" viewBox="0 0 16 16"><path d="M3 2h3l1.5 3.5-2 1.3a8 8 0 0 0 3.7 3.7l1.3-2L14 10v3a1 1 0 0 1-1 1A11 11 0 0 1 2 3a1 1 0 0 1 1-1z"/></svg>
        555-018-2734
      </p>
      <p class="contact__line">
        <svg class="contact__icon" viewBox="0 0 16 16"><path d="M1 3h14v10H1z M2 4l6 5 6-5" fill="none" stroke="#6a6a6a" stroke-width="1.4"/></svg>
        hello@silvermiststudio.com
      </p>
      <p class="contact__line">
        <svg class="contact__icon" viewBox="0 0 16 16"><circle cx="8" cy="8" r="6.3" fill="none" stroke="#6a6a6a" stroke-width="1.4"/><path d="M1.7 8h12.6M8 1.7c-3 3.5-3 9 0 12.6M8 1.7c3 3.5 3 9 0 12.6" fill="none" stroke="#6a6a6a" stroke-width="1.1"/></svg>
        www.silvermiststudio.com
      </p>
    </div>

    <div class="appointment">
      <span class="appointment__field">Date:<span class="appointment__rule appointment__rule--date"></span></span>
      <span class="appointment__field">Time:<span class="appointment__rule appointment__rule--time"></span></span>
    </div>
  </section>
</body>
</html>
```